Word Template for Communications, Reports

I. A Word template for External Reports and a Word template for External Communications
1.Create a template in Word for reports and another template in Word for sending external communications.
1.1. Predefined and locked text styles.
1.2. Quick elements fields (custom) that allow the integration of basic information of each document.
1.3. Professional design and that administrators can place it to different projects.

II. Job postings
We also want a template in Word to make vacancy postings, to facilitate the job of recruiting staff.
Updates

Target Market(s)

External clients (our main clients are public institutions of the government of the Dominican Republic.)

Industry/Entity Type

Construcción

Font styles to use
Serif
Other font styles liked:
• Arial, Book Antiqua

Colors
EE7325
F08F49
F5BC92
FAE3D3
FDF4ED
EB3D1F
EC4F4E
F09395
F8D3D4
FCEDEE

Requirements
Nice to have
• Since we are a group of about 4 companies, I would like each template to be used by any of the companies

```html
<!DOCTYPE html>
<html lang="en">
<head>
<meta charset="utf-8">
<title>Arven – Document Templates</title>
<link rel="stylesheet" href="https://fonts.googleapis.com/css2?family=Gelasio:wght@400;500;600;700&display=swap">
<style>
  :root {
    --red: #eb3d1f;
    --orange: #ee7325;
    --orange-mid: #f08f49;
    --peach: #f5bc92;
    --peach-light: #fae3d3;
    --cream: #fdf4ed;
    --black: #0b0b0b;
    --grey: #6d6e71;
    --stage: #c8c9cb;
    --paper: #ffffff;
    --text: #231f20;
  }
  * { box-sizing: border-box; margin: 0; padding: 0; }
  html, body { width: 1099px; height: 1200px; overflow: hidden; background: var(--stage); }
  body { font-family: "Gelasio", "Book Antiqua", serif; color: var(--text); }
  .canvas { position: relative; width: 1099px; height: 1200px; background: var(--stage); overflow: hidden; }

  .page { position: absolute; background: var(--paper); overflow: hidden; }
  .page--portrait { width: 355px; height: 502px; }
  .page--landscape { width: 503px; height: 355px; }
  .page--cover { left: 164px; top: 52px; }
  .page--terms { left: 653px; top: 52px; }
  .page--comms { left: 90px; top: 613px; }
  .page--letter { left: 653px; top: 613px; }

  .abs { position: absolute; }

  /* Cover */
  .cover-art { position: absolute; inset: 0; width: 355px; height: 502px; }
  .cover-title { position: absolute; left: 15px; top: 250px; font-weight: 700; font-size: 16px; line-height: 18px; color: var(--black); letter-spacing: 0.2px; }
  .cover-title .accent { color: var(--red); }
  .cover-brand { position: absolute; left: 14px; top: 329px; font-weight: 700; font-size: 46px; letter-spacing: 3px; color: var(--black); line-height: 1; }
  .cover-for { position: absolute; left: 15px; top: 389px; }
  .cover-for h2 { font-size: 13.5px; font-weight: 700; color: var(--black); margin-bottom: 2px; }
  .cover-for p { font-size: 11px; font-weight: 400; line-height: 14.3px; color: var(--black); }

  /* Page header */
  .page-header { position: absolute; left: 0; right: 0; top: 0; height: 36px; }
  .page-header .brand { position: absolute; font-weight: 700; font-size: 12.5px; letter-spacing: 1.5px; color: var(--black); line-height: 1; }
  .page-header .rule-top { position: absolute; right: 0; height: 2px; background: var(--black); }
  .page-header .rule-bottom { position: absolute; right: 0; height: 2px; background: var(--red); }
  .page-header .title { position: absolute; font-weight: 700; font-size: 12px; line-height: 1; color: var(--red); white-space: nowrap; }
  .page-header .title span { color: var(--grey); }

  .page--portrait .brand { left: 21px; top: 21px; }
  .page--portrait .rule-top { left: 66px; top: 18px; }
  .page--portrait .rule-bottom { left: 66px; top: 33px; }
  .page--portrait .title { left: 113px; top: 21px; }

  .page--landscape .brand { left: 53px; top: 21px; }
  .page--landscape .rule-top { left: 98px; top: 16px; }
  .page--landscape .rule-bottom { left: 98px; top: 32px; }
  .page--landscape .title { left: 166px; top: 20px; }

  /* Body text */
  .copy { font-size: 6.4px; line-height: 9.6px; color: var(--text); font-weight: 400; }
  .copy--justify { text-align: justify; }
  .bullets { list-style: none; }
  .bullets li { position: relative; padding-left: 22px; }
  .bullets li::before { content: ""; position: absolute; left: 13px; top: 3.4px; width: 3px; height: 3px; border-radius: 50%; background: var(--black); }
  .note-label { font-weight: 700; color: var(--black); }

  /* Steps */
  .steps { position: absolute; left: 0; top: 150px; width: 355px; height: 120px; }
  .step-num { font-family: "Gelasio", "Book Antiqua", serif; font-size: 13px; font-weight: 400; fill: var(--black); }
  .step-caption { position: absolute; top: 261px; width: 60px; text-align: center; }
  .step-caption h3 { font-size: 5px; font-weight: 700; color: var(--black); margin-bottom: 1px; line-height: 6px; }
  .step-caption p { font-size: 3.2px; line-height: 4.2px; color: var(--text); }

  .illustration { position: absolute; left: 20px; top: 326px; width: 121px; height: 96px; background: linear-gradient(135deg, var(--red) 0%, #d8331a 55%, var(--orange) 100%); }

  /* Footer */
  .page-footer { position: absolute; left: 0; height: 15px; background: var(--black); color: #fff; font-size: 6.2px; line-height: 15px; font-weight: 500; white-space: nowrap; }
  .page-footer .mark { position: absolute; right: -11px; top: 2px; width: 11px; height: 11px; background: var(--orange); }
  .page-number { position: absolute; font-size: 6.2px; font-weight: 500; color: var(--black); }
  .page--portrait .page-footer { top: 469px; width: 240px; padding-left: 21px; }
  .page--portrait .page-number { left: 327px; top: 473px; }
  .page--landscape .page-footer { top: 327px; width: 240px; padding-left: 53px; }
  .page--landscape .page-number { left: 476px; top: 331px; }

  /* Table */
  .plan-table { position: absolute; left: 53px; top: 53px; display: grid; grid-template-columns: 68px 74px 75px 74px 95px; grid-template-rows: 24px repeat(7, 31px); column-gap: 2.7px; row-gap: 2.4px; }
  .plan-table .th { display: flex; align-items: center; justify-content: center; text-align: center; color: #fff; font-size: 5.8px; line-height: 6.6px; font-weight: 700; padding: 0 3px; }
  .th--red { background: var(--red); }
  .th--black { background: var(--black); }
  .plan-table .row-label { display: flex; align-items: center; justify-content: center; font-size: 5.8px; font-weight: 700; color: var(--black); }
  .row-label--light { background: var(--cream); border-left: 2px solid var(--peach-light); }
  .row-label--dark { background: var(--peach-light); border-left: 2px solid var(--peach); }
  .plan-table .cell { display: flex; align-items: center; justify-content: center; font-size: 5.4px; font-weight: 700; color: var(--black); border: 1px solid var(--black); }
  .cell--red { border-color: var(--red) !important; }

  /* Letter */
  .letter-meta { font-size: 6.4px; line-height: 10.5px; color: var(--black); }
  .letter-meta .blank { display: inline-block; width: 50px; border-bottom: 0.6px solid var(--black); margin-left: 2px; }
  .letter-fields p { font-size: 6.4px; line-height: 10.7px; font-weight: 700; color: var(--black); }
  .salutation { font-size: 8.6px; font-weight: 700; color: var(--black); }
  .signature { position: absolute; left: 29px; top: 428px; width: 40px; height: 18px; background: linear-gradient(90deg, rgba(235,61,31,0.28), rgba(238,115,37,0.08)); }
</style>
</head>
<body>
<main class="canvas">

  <!-- Cover -->
  <section class="page page--portrait page--cover">
    <svg class="cover-art" viewBox="0 0 597 845" width="355" height="502">
      <defs>
        <linearGradient id="plantTones" x1="0" y1="0" x2="1" y2="1">
          <stop offset="0" stop-color="#8fb9c9"/>
          <stop offset="0.35" stop-color="#5e7f8c"/>
          <stop offset="0.6" stop-color="#c9a46a"/>
          <stop offset="0.8" stop-color="#6a6d6c"/>
          <stop offset="1" stop-color="#3c3f42"/>
        </linearGradient>
        <linearGradient id="accentFade" x1="0" y1="1" x2="1" y2="0">
          <stop offset="0" stop-color="#eb3d1f"/>
          <stop offset="1" stop-color="#ee7325"/>
        </linearGradient>
      </defs>
      <polygon points="0,0 376,0 126,250 0,124" fill="#141416"/>
      <polygon points="0,142 120,262 0,382" fill="var(--red)"/>
      <g role="img" aria-label="Photo of industrial pipework with pressure gauges in a plant room">
        <polygon points="392,0 597,0 597,845 172,845 436,580 136,280" fill="url(#plantTones)"/>
      </g>
      <polygon points="172,845 436,580 597,740 597,845" fill="url(#accentFade)" opacity="0.92"/>
    </svg>
    <h1 class="cover-title">SANITARY<br><span class="accent">INFRASTRUCTURE</span><br>WORKS</h1>
    <div class="cover-brand">ARVEN</div>
    <div class="cover-for">
      <h2>PERPOSAL FOR:</h2>
      <p>Linden Court II<br>RESERVE STUDY<br>HALVER RESERVE STUDY+</p>
    </div>
  </section>

  <!-- Terms & Conditions -->
  <section class="page page--portrait page--terms">
    <header class="page-header">
      <div class="brand">ARVEN</div>
      <div class="rule-top"></div>
      <div class="rule-bottom"></div>
      <h2 class="title">TERMS &amp; <span>CONDITIONS</span></h2>
    </header>

    <p class="copy abs" style="left:20px; top:50px; width:314px;">The pricing stated is valid for a period of forty-five (45) days from the date of the proposal. If not all required inform ation is received within ninety (90) days, we reserve the right to increase the pricing stated in this proposal.</p>
    <ul class="copy bullets abs" style="left:20px; top:88px; width:314px;">
      <li>Payment is due within thirty (30) days of invoice receipt.</li>
      <li>Payment is due within thirty (30) days of invoice receipt.</li>
      <li>Payment is due within thirty (30) days of invoice receipt.</li>
    </ul>
    <p class="copy abs" style="left:20px; top:127px; width:314px;">here is a 1.5 percent (1.5%) finance charge on outstanding balances for each thirty (30) days, or portion thereof, overdue. If payment of our invoice(s) is not made within thirty (30) days, and we turn your.</p>

    <svg class="steps" viewBox="0 150 355 120" width="355" height="120">
      <defs>
        <marker id="arrowHead" viewBox="0 0 6 6" refX="5" refY="3" markerWidth="5" markerHeight="5" orient="auto">
          <path d="M0 0 L6 3 L0 6 Z" fill="var(--red)"/>
        </marker>
      </defs>
      <g fill="none" stroke="var(--red)" stroke-width="0.9">
        <path d="M73 181 Q107 143 139 178" marker-end="url(#arrowHead)"/>
        <path d="M142 181 Q177 143 209 178" marker-end="url(#arrowHead)"/>
        <path d="M212 181 Q246 143 278 178" marker-end="url(#arrowHead)"/>
      </g>
      <g class="step">
        <path d="M55.3 201.3 A25 25 0 1 0 90.7 201.3" fill="none" stroke="var(--red)" stroke-width="12"/>
        <path d="M47 204 A31 31 0 0 1 58 191" fill="none" stroke="var(--black)" stroke-width="0.8"/>
        <path d="M88 191 A31 31 0 0 1 99 204" fill="none" stroke="var(--black)" stroke-width="0.8"/>
        <circle cx="73" cy="181" r="1.6" fill="#fff" stroke="var(--red)" stroke-width="0.8"/>
        <circle cx="73" cy="219" r="17" fill="#fff" stroke="var(--black)" stroke-width="1"/>
        <text class="step-num" x="73" y="198" text-anchor="middle">01</text>
        <g fill="none" stroke="var(--black)" stroke-width="0.8">
          <path d="M70 222 Q66 218 67.5 214 Q69 210 73 210 Q77 210 78.5 214 Q80 218 76 222 Z"/>
          <line x1="70.5" y1="224.5" x2="75.5" y2="224.5"/>
          <line x1="71" y1="226.5" x2="75" y2="226.5"/>
        </g>
      </g>
      <g class="step">
        <path d="M124.3 201.3 A25 25 0 1 0 159.7 201.3" fill="none" stroke="var(--red)" stroke-width="12"/>
        <path d="M116 204 A31 31 0 0 1 127 191" fill="none" stroke="var(--black)" stroke-width="0.8"/>
        <path d="M157 191 A31 31 0 0 1 168 204" fill="none" stroke="var(--black)" stroke-width="0.8"/>
        <circle cx="142" cy="181" r="1.6" fill="#fff" stroke="var(--red)" stroke-width="0.8"/>
        <circle cx="142" cy="219" r="17" fill="#fff" stroke="var(--black)" stroke-width="1"/>
        <text class="step-num" x="142" y="198" text-anchor="middle">02</text>
        <g fill="var(--black)">
          <rect x="133" y="218" width="2.5" height="6"/>
          <rect x="137" y="215" width="2.5" height="9"/>
          <rect x="141" y="219" width="2.5" height="5"/>
          <rect x="145" y="214" width="2.5" height="10"/>
          <rect x="149" y="216" width="2.5" height="8"/>
          <rect x="132" y="224.5" width="20" height="0.9"/>
        </g>
      </g>
      <g class="step">
        <path d="M194.3 201.3 A25 25 0 1 0 229.7 201.3" fill="none" stroke="var(--red)" stroke-width="12"/>
        <path d="M186 204 A31 31 0 0 1 197 191" fill="none" stroke="var(--black)" stroke-width="0.8"/>
        <path d="M227 191 A31 31 0 0 1 238 204" fill="none" stroke="var(--black)" stroke-width="0.8"/>
        <circle cx="212" cy="181" r="1.6" fill="#fff" stroke="var(--red)" stroke-width="0.8"/>
        <circle cx="212" cy="219" r="17" fill="#fff" stroke="var(--black)" stroke-width="1"/>
        <text class="step-num" x="212" y="198" text-anchor="middle">03</text>
        <g fill="none" stroke="var(--black)" stroke-width="0.8">
          <circle cx="212" cy="219" r="6"/>
          <circle cx="212" cy="219" r="3"/>
          <line x1="212" y1="210" x2="212" y2="228"/>
          <line x1="203" y1="219" x2="221" y2="219"/>
        </g>
        <circle cx="212" cy="219" r="1" fill="var(--black)"/>
      </g>
      <g class="step">
        <path d="M263.3 201.3 A25 25 0 1 0 298.7 201.3" fill="none" stroke="var(--red)" stroke-width="12"/>
        <path d="M255 204 A31 31 0 0 1 266 191" fill="none" stroke="var(--black)" stroke-width="0.8"/>
        <path d="M296 191 A31 31 0 0 1 307 204" fill="none" stroke="var(--black)" stroke-width="0.8"/>
        <circle cx="281" cy="181" r="1.6" fill="#fff" stroke="var(--red)" stroke-width="0.8"/>
        <circle cx="281" cy="219" r="17" fill="#fff" stroke="var(--black)" stroke-width="1"/>
        <text class="step-num" x="281" y="198" text-anchor="middle">04</text>
        <g fill="none" stroke="var(--black)" stroke-width="0.8">
          <circle cx="281" cy="220" r="6.5"/>
          <circle cx="281" cy="211.5" r="1.5"/>
          <path d="M278 223 L280 219 L284 217 L282 221 Z" fill="var(--black)"/>
        </g>
      </g>
    </svg>

    <div class="step-caption" style="left:43px;"><h3>Title One</h3><p>Sed ut perspiciatis unde omnis iste natus error sit volupta accusan dolor laudan totam</p></div>
    <div class="step-caption" style="left:112px;"><h3>Title Two</h3><p>Sed ut perspiciatis unde omnis iste natus error sit volupta accusan dolor laudan totam</p></div>
    <div class="step-caption" style="left:182px;"><h3>Title Three</h3><p>Sed ut perspiciatis unde omnis iste natus error sit volupta accusan dolor laudan totam</p></div>
    <div class="step-caption" style="left:251px;"><h3>Title Four</h3><p>Sed ut perspiciatis unde omnis iste natus error sit volupta accusan dolor laudan totam</p></div>

    <p class="copy abs" style="left:20px; top:291px; width:314px;">The pricing stated is valid for a period of forty-five (45) days from the date of the proposal. If not all required inform ation is received within ninety (90) days, we reserve the right to increase the pricing stated in this proposal.</p>

    <div class="illustration" role="img" aria-label="Illustration of two plumbing technicians servicing wall pipework"></div>

    <div class="abs" style="left:146px; top:326px; width:188px;">
      <p class="copy copy--justify">The pricing stated is valid for a period of forty-five (45) days from the date of the proposal. If not all required inform ation is received within ninety (90) days, we reserve the right to increase the pricing stated in this proposal.</p>
      <p class="copy copy--justify" style="margin-top:9.6px;">Payment is due within thirty (30) days of invoice receipt. There is a 1.5 percent (1.5%) finance charge on outstanding balances for each thirty (30) days, or portion thereof, overdue. If payment of our invoice(s) is not made within thirty (30) days, and we turn your account over to an attorney for .</p>
    </div>

    <div class="copy abs" style="left:20px; top:428px; width:314px;">
      <p class="note-label">Note:</p>
      <p>Lorem ipsum dolor sit amet, consectetuer adipiscing elit, sed diam nonummy nibh euismod nostrud exerci tation ullamcorper suscipit lobortis nisl ut aliquip ex ea commodo consequat. Duis autem vel eum iriure dolor in hendrerit in vulputate</p>
    </div>

    <footer class="page-footer">48 Marlow Ave. Brightvale, NJ 07190 | P: 10-555-0142 | F: 732-555-0187<span class="mark"></span></footer>
    <div class="page-number">01</div>
  </section>

  <!-- Communication material -->
  <section class="page page--landscape page--comms">
    <header class="page-header">
      <div class="brand">ARVEN</div>
      <div class="rule-top"></div>
      <div class="rule-bottom"></div>
      <h2 class="title">COMMUNICATION <span>MATERIAL</span></h2>
    </header>

    <div class="plan-table" role="table" aria-label="Communication plan">
      <div class="th th--red">Communication<br>Plan Situation</div>
      <div class="th th--black">Level of<br>Urgency (1-4)</div>
      <div class="th th--red">Stakeholder(s)<br>DRI</div>
      <div class="th th--black">Objectives<br>and Goals</div>
      <div class="th th--red">Required Actions,<br>Messaging &amp; Content</div>

      <div class="row-label row-label--light">One</div>
      <div class="cell">TEXT HERE</div><div class="cell">TEXT HERE</div><div class="cell">TEXT HERE</div><div class="cell">TEXT HERE</div>

      <div class="row-label row-label--dark">Two</div>
      <div class="cell cell--red">TEXT HERE</div><div class="cell cell--red">TEXT HERE</div><div class="cell cell--red">TEXT HERE</div><div class="cell cell--red">TEXT HERE</div>

      <div class="row-label row-label--light">Three</div>
      <div class="cell">TEXT HERE</div><div class="cell">TEXT HERE</div><div class="cell">TEXT HERE</div><div class="cell">TEXT HERE</div>

      <div class="row-label row-label--dark">Four</div>
      <div class="cell cell--red">TEXT HERE</div><div class="cell cell--red">TEXT HERE</div><div class="cell cell--red">TEXT HERE</div><div class="cell cell--red">TEXT HERE</div>

      <div class="row-label row-label--light">Five</div>
      <div class="cell">TEXT HERE</div><div class="cell">TEXT HERE</div><div class="cell">TEXT HERE</div><div class="cell">TEXT HERE</div>

      <div class="row-label row-label--dark">Six</div>
      <div class="cell cell--red">TEXT HERE</div><div class="cell cell--red">TEXT HERE</div><div class="cell cell--red">TEXT HERE</div><div class="cell cell--red">TEXT HERE</div>

      <div class="row-label row-label--light">Seven</div>
      <div class="cell">TEXT HERE</div><div class="cell">TEXT HERE</div><div class="cell">TEXT HERE</div><div class="cell">TEXT HERE</div>
    </div>

    <footer class="page-footer">SANITARY&nbsp; INFRASTRUCTURE WORKS<span class="mark"></span></footer>
    <div class="page-number">01</div>
  </section>

  <!-- Official communication letter -->
  <section class="page page--portrait page--letter">
    <header class="page-header">
      <div class="brand">ARVEN</div>
      <div class="rule-top"></div>
      <div class="rule-bottom"></div>
      <h2 class="title">OFFICIAL <span>COMMUNICATION</span></h2>
    </header>

    <p class="letter-meta abs" style="left:27px; top:73px;">Date:<span class="blank"></span></p>
    <p class="letter-meta abs" style="left:265px; top:73px;">Ref:<span class="blank"></span></p>

    <div class="letter-fields abs" style="left:27px; top:88px;">
      <p>Contract: lorem ipsum</p>
      <p>Affair: lorem ipsum</p>
      <p>Attachments: lorem ipsum</p>
    </div>

    <p class="salutation abs" style="left:27px; top:140px;">Dear, Arven</p>

    <div class="abs" style="left:27px; top:157px; width:305px;">
      <p class="copy copy--justify">Lorem ipsum dolor sit amet, consectetuer adipiscing elit, sed diam nonummy nibh euismod nostrud exerci tation ullamcorper suscipit lobortis nisl ut aliquip ex ea commodo consequat. Duis autem vel eum iriure dolor in hendrerit in vulputate velit esse molestie consequat, vel illum dolore eu feugiat nulla facilisis at vero eros et accumsan et iusto odio dignissim qui blandit praesent luptatum zzril delenit augue duis dolore te feugait nulla facilisi.Lorem ipsum dolor sit amet, consectetuer adipiscing elit, sed diam nonummy nibh euismod nostrud exerci tation ullamcorper suscipit lobortis nisl ut aliquip ex ea commodo consequat.</p>
      <p class="copy copy--justify" style="margin-top:9.6px;">Duis autem vel eum iriure dolor in hendrerit in vulputate velit esse molestie consequat, vel illum dolore eu feugiat nulla facilisis at vero eros et accumsan et iusto odio dignissim qui blandit praesent luptatum zzril delenit augue duis dolore te feugait nulla facilisi.Lorem ipsum dolor sit amet, consectetuer adipiscing elit, sed diam nonummy nibh euismod nostrud exerci tation ullamcorper suscipit lobortis nisl ut aliquip ex ea commodo consequat. Duis autem vel eum iriure dolor in hendrerit in vulputate velit esse molestie consequat, vel illum dolore eu feugiat nulla facilisis at vero eros et accumsan et iusto odio dignissim qui blandit praesent luptatum zzril delenit augue duis dolore te feugait nulla facilisi.</p>
      <p class="copy copy--justify" style="margin-top:9.6px;">Lorem ipsum dolor sit amet, consectetuer adipiscing elit, sed diam nonummy nibh euismod nostrud exerci tation ullamcorper suscipit lobortis nisl ut aliquip ex ea commodo consequat. Duis autem vel eum iriure dolor in hendrerit in vulputate velit esse molestie consequat, vel illum dolore eu feugiat nulla facilisis at vero eros et accumsan et iusto odio dignissim qui blandit praesent luptatum zzril delenit augue duis dolore te feugait nulla facilisi.</p>
    </div>

    <div class="signature" role="img" aria-label="Handwritten signature of the sender"></div>

    <footer class="page-footer">48 Marlow Ave. Brightvale, NJ 07190 | P: 10-555-0142 | F: 732-555-0187<span class="mark"></span></footer>
    <div class="page-number">01</div>
  </section>

</main>
</body>
</html>
```